11th Annual Vemtora Forum Flyer - Save the Date

We need a flyer for our annual Forum that will be creative with the theme of the Forum while highlighting our conference Title and Topics. Flyer should allow for a header that can be used consistently across conference communication. This is our 11th Annual Forum, which will take place outside of Houston, Texas at Bel Costano Resort and Spa.

Target Market(s)

Architects, engineers, contractors, universities, building project Owners

Industry/Entity Type

Construction

Font styles to use
Sans Serif

Colors

Designer to choose colors to be used in the design.

Requirements
Must have
• Title, date, location, key topics (title only), logo. See attached for breakdown of information.
Nice to have
• Creativity with the theme of the Forum, ability to slice flyer so that a portion can be used for a header in other conference documents.
• Mention of Closing Keynote, Dale Hutton
Should not have
• Please don't use the topic descriptions in the Flyer. Just the main titles of the topics is necessary.
• Should not be too word, but eye-catching with graphics and main

```html
<!DOCTYPE html>
<html lang="en">
<head>
<meta charset="utf-8">
<title>11th Vemtora Annual Forum – Save the Date</title>
<link rel="stylesheet" href="https://fonts.googleapis.com/css2?family=Montserrat:wght@600;700;800&family=Roboto:wght@400;500;700&family=Roboto+Condensed:wght@400;500;700&display=swap">
<style>
  :root {
    --navy-deep: #1b2460;
    --navy: #23358f;
    --blue-glow: #2f7fd6;
    --green: #8cc63f;
    --ink: #231f20;
    --row-dark: #262324;
    --band-grey: #e4e4e4;
    --gap-grey: #d9d9d9;
    --white: #ffffff;
    --sky-top: #4f7fc4;
    --sky-mid: #8fb4e2;
    --sky-low: #c9d9ef;
  }
  * { box-sizing: border-box; margin: 0; padding: 0; }
  html, body { width: 927px; height: 1200px; overflow: hidden; background: var(--white); }
  .flyer {
    position: relative; width: 927px; height: 1200px; overflow: hidden;
    background: var(--gap-grey);
    font-family: "Roboto", Arial, sans-serif;
  }
  .hero-photo {
    position: absolute; left: 0; top: 0; width: 927px; height: 372px;
    background: linear-gradient(160deg, var(--sky-top) 0%, var(--sky-mid) 45%, var(--sky-low) 70%, #6d8fc0 100%);
  }
  .logo-tab { position: absolute; left: 83px; top: 0; width: 292px; height: 132px; }
  .logo-tab svg { position: absolute; inset: 0; }
  .logo-lockup {
    position: absolute; left: 40px; top: 34px; display: flex; align-items: center; gap: 14px;
  }
  .logo-mark { width: 56px; height: 56px; border-radius: 50%; background: var(--navy); }
  .logo-name {
    font-family: "Montserrat", Arial, sans-serif; font-weight: 700; font-size: 34px; color: #4a4a4a;
  }
  .save-the-date {
    position: absolute; left: 340px; top: 160px; width: 200px; text-align: center;
    font-family: "Montserrat", Arial, sans-serif; font-weight: 700; font-size: 60px; line-height: 62px;
    color: var(--white); letter-spacing: 1px;
  }
  .theme-bar {
    position: absolute; left: 250px; top: 372px; width: 677px; height: 120px; background: var(--green);
  }
  .theme-title {
    position: absolute; left: 320px; top: 391px; width: 560px; text-align: left;
    font-family: "Montserrat", Arial, sans-serif; font-weight: 800; font-size: 31px; line-height: 42px;
    color: var(--ink); letter-spacing: 2.4px;
  }
  .theme-title .second-line { display: block; padding-left: 14px; }
  .topics-band {
    position: absolute; left: 250px; top: 492px; width: 677px; height: 80px;
    background: linear-gradient(180deg, #f2f2f2, var(--band-grey));
  }
  .topics-heading {
    position: absolute; left: 443px; top: 510px;
    font-family: "Montserrat", Arial, sans-serif; font-weight: 700; font-size: 31px; color: var(--ink);
  }
  .topic-row {
    position: absolute; left: 250px; width: 677px; height: 145px; background: var(--row-dark);
  }
  .topic-label {
    position: absolute; left: 444px; font-family: "Montserrat", Arial, sans-serif; font-weight: 700;
    font-size: 22px; line-height: 31px; color: var(--white);
  }
  .topic-label .accent { color: var(--green); }
  .topic-photo {
    position: absolute; left: 672px; width: 243px; height: 130px;
    clip-path: polygon(0 0, 100% 0, 100% 100%, 14% 100%);
  }
  .photo-contract { background: linear-gradient(135deg, #eef1f4, #b9c2cc 60%, #d9dde2); }
  .photo-culture { background: linear-gradient(135deg, #6b5a48, #3d3a36 55%, #8a7a66); }
  .photo-site { background: linear-gradient(180deg, #3a4a7a 0%, #d9783a 60%, #f2b24a 75%, #3a2a22 100%); }
  .photo-keynote { background: linear-gradient(135deg, #9fbf7a, #5f7f4a 55%, #2c3550); }
  .keynote-label {
    position: absolute; left: 507px; top: 1080px; font-family: "Roboto", Arial, sans-serif;
    font-weight: 400; font-size: 17px; color: var(--white);
  }
  .keynote-name {
    position: absolute; left: 495px; top: 1106px; font-family: "Montserrat", Arial, sans-serif;
    font-weight: 700; font-size: 30px; color: var(--green); letter-spacing: 0.5px;
  }
  .side-panel { position: absolute; left: 0; top: 0; width: 927px; height: 1200px; pointer-events: none; }
  .edition-badge {
    position: absolute; left: 61px; top: 321px; width: 144px; height: 144px; border-radius: 50%;
    background: var(--green); color: var(--white); text-align: center;
    font-family: "Montserrat", Arial, sans-serif; font-weight: 700; font-size: 54px; line-height: 144px;
  }
  .edition-badge sup { font-size: 28px; vertical-align: 22px; margin-left: 2px; }
  .forum-title {
    position: absolute; left: 36px; top: 498px; font-family: "Montserrat", Arial, sans-serif; font-weight: 600;
    font-size: 47px; line-height: 62px; color: var(--white);
  }
  .forum-title .brand { display: block; color: var(--green); }
  .forum-when {
    position: absolute; left: 36px; top: 730px; font-family: "Roboto Condensed", Arial, sans-serif;
    font-weight: 700; font-size: 35px; line-height: 46px; color: var(--green);
  }
  .venue-name {
    position: absolute; left: 36px; top: 853px; font-family: "Roboto Condensed", Arial, sans-serif;
    font-weight: 700; font-size: 37px; line-height: 46px; color: var(--white);
  }
  .venue-address {
    position: absolute; left: 36px; top: 974px; font-family: "Roboto", Arial, sans-serif; font-weight: 400;
    font-size: 24px; line-height: 32px; color: var(--green);
  }
  .contact-lead {
    position: absolute; left: 36px; top: 1088px; font-family: "Roboto", Arial, sans-serif; font-weight: 400;
    font-size: 21px; color: var(--white); letter-spacing: 1px;
  }
  .contact-phone {
    position: absolute; left: 36px; top: 1120px; display: flex; align-items: center; gap: 22px;
    font-family: "Roboto", Arial, sans-serif; font-weight: 700; font-size: 26px; color: var(--white);
    letter-spacing: 0.5px;
  }
</style>
</head>
<body>
<main class="flyer">
  <div class="hero-photo" role="img" aria-label="Glass office towers against a blue sky, with a businessman seated on a wooden three-legged stool"></div>

  <div class="logo-tab">
    <svg width="292" height="132" viewBox="0 0 292 132" aria-hidden="true">
      <defs>
        <linearGradient id="tabFill" x1="0" y1="0" x2="0" y2="1">
          <stop offset="0" stop-color="#ffffff"/>
          <stop offset="1" stop-color="#dcdcdc"/>
        </linearGradient>
      </defs>
      <polygon points="0,0 292,0 292,118 146,130 0,118" fill="url(#tabFill)"/>
    </svg>
    <div class="logo-lockup">
      <span class="logo-mark"></span>
      <span class="logo-name">Vemtora</span>
    </div>
  </div>

  <h1 class="save-the-date">SAVE<br>THE<br>DATE</h1>

  <div class="theme-bar"></div>
  <h2 class="theme-title">The Three-legged Stool<span class="second-line">– Balanced or Broken?</span></h2>

  <div class="topics-band"></div>
  <h3 class="topics-heading">Three Key Topics:</h3>

  <section class="topic-row" style="top:573px"></section>
  <p class="topic-label" style="top:601px">The Right<br>Contract<br><span class="accent">Management</span></p>
  <div class="topic-photo photo-contract" style="top:573px;height:145px" role="img" aria-label="Business handshake over a signed contract"></div>

  <section class="topic-row" style="top:727px"></section>
  <p class="topic-label" style="top:765px">The Right<br><span class="accent">Culture</span></p>
  <div class="topic-photo photo-culture" style="top:727px;height:145px;left:676px;width:239px" role="img" aria-label="Team collaborating in a busy open office"></div>

  <section class="topic-row" style="top:881px"></section>
  <p class="topic-label" style="top:920px">The Right<br><span class="accent">Subcontractors</span></p>
  <div class="topic-photo photo-site" style="top:881px;height:145px;left:680px;width:235px" role="img" aria-label="Construction workers on steel framing at sunset"></div>

  <section class="topic-row" style="top:1035px"></section>
  <p class="keynote-label">Closing Keynote</p>
  <p class="keynote-name">Dale Hutton</p>
  <div class="topic-photo photo-keynote" style="top:1035px;height:145px;left:724px;width:191px;clip-path:polygon(0 0,100% 0,100% 100%,14% 100%)" role="img" aria-label="Portrait of closing keynote speaker Dale Hutton"></div>

  <svg class="side-panel" width="927" height="1200" viewBox="0 0 927 1200" aria-hidden="true">
    <defs>
      <radialGradient id="panelGlow" cx="0.3" cy="0.45" r="0.7">
        <stop offset="0" stop-color="#2f7fd6"/>
        <stop offset="0.45" stop-color="#23358f"/>
        <stop offset="1" stop-color="#1b2460"/>
      </radialGradient>
    </defs>
    <polygon points="0,172 250,172 485,1200 0,1200" fill="url(#panelGlow)"/>
  </svg>

  <div class="edition-badge">11<sup>th</sup></div>
  <h2 class="forum-title"><span class="brand">Vemtora</span>Annual<br>Forum</h2>
  <p class="forum-when">September 9 &amp;10<br>8:00 AM to 4:00 PM</p>
  <p class="venue-name">Bel Costano<br>Lake Resort &amp; Spa</p>
  <p class="venue-address">240 Bel Costano Blvd<br>Montgomery, Texas 77356</p>
  <p class="contact-lead">For more information:</p>
  <p class="contact-phone">
    <svg width="24" height="24" viewBox="0 0 24 24" aria-hidden="true">
      <circle cx="12" cy="12" r="11" fill="none" stroke="#ffffff" stroke-width="1.5"/>
      <path d="M8.5 6.5c-.8.4-1.5 1.5-1 3 .8 2.8 3.5 5.8 6.3 7 1.4.6 2.5 0 3-.8l-2-2-1.4.8c-1.3-.6-2.6-2-3.2-3.3l.9-1.3z" fill="#ffffff"/>
    </svg>
    +1 512-555-0148
  </p>
</main>
</body>
</html>
```